Handmade candle business in melbourne requiring assistance with designing classy labels

My business name is Wick and Willow.
I specialise in making handmade candles, i'm based in Melbourne.
My moto is "Delicately hand poured and infused by me...for you"
wickwillow@mailbox-demo.net
0487 913 072

I need some assistance with designing my labels for my glass candles
I really like earthy colours and nothing too bright, but I want it to look classy and elegant and something that stands out from other homemade candle businesses.
I have attached a sample of a design that appeals to me but open to suggestions.

```html
<!DOCTYPE html>
<html lang="en">
<head>
<meta charset="utf-8">
<title>Wick and Willow – Candle Label</title>
<link href="https://fonts.googleapis.com/css2?family=Pinyon+Script&family=Arimo:wght@400&family=Open+Sans:wght@600&display=swap" rel="stylesheet">
<style>
  :root {
    --maroon: #7d0a26;
    --ink: #111111;
    --label-edge: #efe96a;
    --label-glow: #fdfcb4;
    --band-tone: #e9d9a0;
    --page: #ffffff;
  }
  html, body {
    margin: 0;
    padding: 0;
    width: 1200px;
    height: 759px;
    overflow: hidden;
    background: var(--page);
  }
  .label {
    position: relative;
    width: 1200px;
    height: 759px;
  }
  .label-frame {
    position: absolute;
    inset: 0;
  }
  .motto-lead,
  .motto-line,
  .email-name,
  .email-domain,
  .phone {
    position: absolute;
    left: 0;
    width: 100%;
    text-align: center;
    margin: 0;
    white-space: nowrap;
  }
  .motto-lead {
    top: 70px;
    font-family: "Pinyon Script", cursive;
    font-size: 132px;
    line-height: 1;
    color: var(--maroon);
  }
  .motto-line {
    font-family: "Pinyon Script", cursive;
    font-size: 66px;
    line-height: 1;
    color: var(--ink);
  }
  .motto-line.first { top: 262px; }
  .motto-line.second { top: 362px; }
  .email-name {
    top: 502px;
    font-family: "Arimo", sans-serif;
    font-size: 84px;
    line-height: 1;
    letter-spacing: -3px;
    color: var(--maroon);
  }
  .email-domain {
    top: 583px;
    left: 440px;
    width: auto;
    text-align: left;
    font-family: "Arimo", sans-serif;
    font-size: 17px;
    letter-spacing: 3px;
    text-transform: uppercase;
    color: var(--ink);
  }
  .phone {
    top: 633px;
    font-family: "Open Sans", sans-serif;
    font-weight: 600;
    font-size: 41px;
    line-height: 1;
    color: var(--ink);
  }
</style>
</head>
<body>
  <main class="label">
    <svg class="label-frame" width="1200" height="759" viewBox="0 0 1200 759">
      <defs>
        <linearGradient id="labelFill" x1="0" y1="0" x2="0" y2="1">
          <stop offset="0" stop-color="var(--label-edge)"/>
          <stop offset="0.5" stop-color="var(--label-glow)"/>
          <stop offset="1" stop-color="var(--label-edge)"/>
        </linearGradient>
      </defs>
      <rect class="frame-outer" x="0" y="0" width="1200" height="759" rx="48" fill="var(--maroon)"/>
      <rect class="label-face" x="13" y="13" width="1174" height="733" rx="38" fill="url(#labelFill)"/>
      <path class="suit-border" role="img" aria-label="Decorative border of red and black playing-card suits"
            fill="var(--band-tone)" fill-rule="evenodd"
            d="M51 16 H1149 A35 35 0 0 1 1184 51 V708 A35 35 0 0 1 1149 743 H51 A35 35 0 0 1 16 708 V51 A35 35 0 0 1 51 16 Z
               M78 58 H1122 A20 20 0 0 1 1142 78 V681 A20 20 0 0 1 1122 701 H78 A20 20 0 0 1 58 681 V78 A20 20 0 0 1 78 58 Z"/>
    </svg>

    <h1 class="motto-lead">Delicately</h1>
    <p class="motto-line first">hand poured and infused</p>
    <p class="motto-line second">by me...for you</p>

    <p class="email-name">wickwillow</p>
    <p class="email-domain">@mailbox-demo.net</p>
    <p class="phone">0487 913 072</p>
  </main>
</body>
</html>
```